A Clear Three Step Roadmap For Contractors

We are looking for a one-pager "roadmap" that is similar to the 2nd picture we attached, but much more professional & better... please make it landscape orientation. The logo for this system is attached below, as well.

Our Brand Colors to use:
#f2d582
#303030
#8b8c90

The copy we'd like to use on the flyer:
A Clear Three Step Roadmap that will finally allow you to attract quality customers and win more jobs.

The Ironvale Keystone Method is a simple to follow system that was created specifically for Contractors and Blue Collar Business Owners.

When it comes to marketing and growing their business, the majority of Contractors are left confused, frustrated and extremely overwhelmed. Unlike most sales, marketing & training programs that offer a single "piece of the puzzle", we've mapped out each essential step of the puzzle and cut out all of the fluff.

All you have to do is complete each step in the right order and we'll be guiding you along the entire journey!

A ---> B

Blueprint: Get clear on where you're going, define your ideal audience, and finally, master your message.
Step 1: Clarify The Chaos
Step 2: Define Your Customer
Step 3: Master Your Message

Build: Attract quality leads, Build your funnel and Formulate a high-converting follow-up system
Step 4: Develop Lead Generator
Step 5: Construct Your Funnel
Step 6: Formulate the Follow-Up

Breakthrough: Get in front of your ideal customers and rapidly scale your business by driving traffic and becoming the authority in your market
Step 7: Turn-On the Traffic
Step 8: Become the Authority
Step 9: Unlock Your Growth

```html
<!DOCTYPE html>
<html lang="en">
<head>
<meta charset="utf-8">
<title>Ironvale Keystone Method – A Clear Three Step Roadmap</title>
<link rel="stylesheet" href="https://fonts.googleapis.com/css2?family=Lato:ital,wght@0,400;0,700;0,900;1,900&family=Titillium+Web:ital,wght@1,700&display=swap">
<style>
  :root {
    --gold: #f2d582;
    --gold-deep: #dcc069;
    --gold-pale: #f7e7ae;
    --ink: #303030;
    --ink-deep: #222222;
    --steel: #8b8c90;
    --paper: #ffffff;
    --paper-shade: #dcdcdc;
  }
  * { box-sizing: border-box; margin: 0; padding: 0; }
  html, body { width: 1200px; height: 770px; overflow: hidden; }
  body {
    position: relative;
    font-family: "Lato", Arial, sans-serif;
    color: var(--ink-deep);
    background: linear-gradient(180deg, var(--paper) 20%, var(--paper-shade) 100%);
  }

  /* Header band */
  .header-band {
    position: absolute; left: 0; top: 0; width: 1200px; height: 158px;
    background: linear-gradient(90deg, var(--gold-deep), var(--gold) 50%, var(--gold-deep));
  }
  .brand-box {
    position: absolute; left: 52px; top: 24px; width: 386px; height: 108px;
    background: var(--paper); border: 4px solid var(--ink);
    border-radius: 4px; box-shadow: inset 0 0 0 4px var(--paper), inset 0 0 0 6px var(--steel);
    display: flex; align-items: center; gap: 16px; padding: 0 22px;
  }
  .brand-mark { width: 18px; height: 18px; background: var(--gold-deep); flex: none; }
  .brand-name {
    font-weight: 900; font-size: 30px; line-height: 1.05; color: var(--ink);
    text-transform: uppercase; letter-spacing: 0.5px;
  }
  .tagline {
    position: absolute; left: 480px; top: 36px; width: 690px;
    font-family: "Titillium Web", Arial, sans-serif; font-style: italic; font-weight: 700;
    font-size: 27px; line-height: 36px; text-align: center; color: var(--ink);
  }

  /* Intro copy */
  .intro { position: absolute; left: 73px; top: 170px; width: 1060px; font-size: 14px; font-weight: 700; line-height: 20px; }
  .intro p { margin-bottom: 12px; }
  .intro .closing { width: 480px; }

  /* Road */
  .road {
    position: absolute; left: 0; top: 455px; width: 1200px; height: 240px;
    background: linear-gradient(180deg, var(--ink) 0%, var(--ink-deep) 100%);
  }
  .road-line { position: absolute; left: 0; width: 1200px; height: 4px; background: var(--paper); }
  .road-line.one { top: 16px; }
  .road-line.two { top: 150px; }
  .road-dash {
    position: absolute; left: 560px; width: 640px; height: 3px;
    background: repeating-linear-gradient(90deg, var(--paper) 0 60px, transparent 60px 120px);
  }
  .road-dash.one { top: 83px; }
  .road-dash.two { top: 205px; }

  /* Steps */
  .step {
    position: absolute; left: 52px; width: 490px; height: 118px;
    background: linear-gradient(90deg, var(--gold), var(--gold-pale));
    border-radius: 0 60px 60px 0;
    display: flex; align-items: center; padding-left: 18px;
  }
  .step.blueprint { top: 342px; }
  .step.build { top: 480px; }
  .step.breakthrough { top: 618px; }
  .step-number {
    width: 76px; height: 76px; border-radius: 50%; flex: none;
    border: 3px solid var(--ink); box-shadow: inset 0 0 0 4px var(--gold-pale), inset 0 0 0 6px var(--ink);
    background: var(--paper);
    display: flex; align-items: center; justify-content: center;
    font-weight: 900; font-size: 40px; color: var(--ink-deep);
  }
  .step-text { margin-left: 18px; }
  .step-title { font-weight: 900; font-size: 36px; line-height: 38px; color: var(--ink-deep); letter-spacing: 0.5px; }
  .step-copy { font-size: 10.5px; font-weight: 700; line-height: 13px; width: 300px; margin-top: 3px; }

  /* Roadmap panel */
  .roadmap-frame {
    position: absolute; left: 575px; top: 282px; width: 560px; height: 460px;
    background: var(--paper); border: 3px solid var(--gold-deep); border-radius: 26px;
    box-shadow: 0 6px 18px rgba(0,0,0,0.25);
  }
  .roadmap {
    position: absolute; left: 20px; top: 20px; width: 514px; height: 414px;
    background: radial-gradient(circle at 40% 30%, #3a3a3a, var(--ink-deep));
  }
  .roadmap svg { display: block; }
  .roadmap text { font-family: "Lato", Arial, sans-serif; }
</style>
</head>
<body>
  <header class="header-band">
    <div class="brand-box">
      <span class="brand-mark"></span>
      <span class="brand-name">Ironvale Keystone<br>Method</span>
    </div>
    <h1 class="tagline">A Clear Three Step Roadmap that will finally allow you to attract quality customers and win more jobs.</h1>
  </header>

  <section class="intro">
    <p>The Ironvale Keystone Method is a simple to follow system that was created specifically for Contractors and Blue Collar Business Owners.</p>
    <p>When it comes to growing their business, the majority of Contractors are left confused, frustrated and extremely overwhelmed. Unlike most sales, marketing &amp; training programs that offer a single "piece of the puzzle", we've mapped out each essential step of the puzzle and cut out all of the fluff.</p>
    <p class="closing">All you have to do is complete each step in the right order and we'll be guiding you along the entire journey!</p>
  </section>

  <div class="road">
    <div class="road-line one"></div>
    <div class="road-line two"></div>
    <div class="road-dash one"></div>
    <div class="road-dash two"></div>
  </div>

  <article class="step blueprint">
    <div class="step-number">1</div>
    <div class="step-text">
      <h2 class="step-title">BLUEPRINT</h2>
      <p class="step-copy">Get clear on where you're going, define your ideal audience, and finally master your message</p>
    </div>
  </article>
  <article class="step build">
    <div class="step-number">2</div>
    <div class="step-text">
      <h2 class="step-title">BUILD</h2>
      <p class="step-copy">Attract quality leads, Build your funnel and Formulate a high-converting follow-up system</p>
    </div>
  </article>
  <article class="step breakthrough">
    <div class="step-number">3</div>
    <div class="step-text">
      <h2 class="step-title">BREAKTHROUGH</h2>
      <p class="step-copy">Get in front of your ideal customers and rapidly scale your business by driving traffic and becoming the authority in your market</p>
    </div>
  </article>

  <div class="roadmap-frame">
    <div class="roadmap">
      <svg width="514" height="414" viewBox="0 0 514 414">
        <defs>
          <radialGradient id="stepIcon" cx="50%" cy="40%" r="60%">
            <stop offset="0" stop-color="#f7e7ae"/>
            <stop offset="1" stop-color="#d9d9d9"/>
          </radialGradient>
        </defs>
        <!-- route -->
        <g stroke="#cfcfcf" stroke-width="1.5" stroke-dasharray="4 4" fill="none">
          <path d="M170 300 H440 V195 H170 V100 H440"/>
          <path d="M118 340 L150 318"/>
        </g>
        <path d="M462 82 L482 72" stroke="#cfcfcf" stroke-width="1.5"/>
        <path d="M476 68 L484 71 L479 78" fill="none" stroke="#cfcfcf" stroke-width="1.5"/>
        <text x="110" y="358" fill="#f2d582" font-size="18" font-weight="900" font-style="italic">A</text>
        <text x="486" y="76" fill="#f2d582" font-size="18" font-weight="900" font-style="italic">B</text>

        <!-- row labels -->
        <g fill="#ffffff" font-size="11" font-weight="700">
          <rect x="10" y="90" width="14" height="18" fill="none" stroke="#ffffff"/>
          <text x="14" y="103" font-size="10">3</text>
          <text x="32" y="103">BREAKTHROUGH</text>
          <rect x="10" y="185" width="14" height="18" fill="none" stroke="#ffffff"/>
          <text x="14" y="198" font-size="10">2</text>
          <text x="32" y="198">BUILD</text>
          <rect x="10" y="290" width="14" height="18" fill="none" stroke="#ffffff"/>
          <text x="14" y="303" font-size="10">1</text>
          <text x="32" y="303">BLUEPRINT</text>
        </g>
        <g stroke="#f2d582" stroke-width="2">
          <path d="M32 110 H118"/><path d="M32 205 H70"/><path d="M32 310 H92"/>
        </g>

        <!-- step icons -->
        <g stroke="#f2d582" stroke-width="2" fill="url(#stepIcon)">
          <circle cx="170" cy="100" r="26" role="img" aria-label="Turn-On the Traffic icon"/>
          <circle cx="305" cy="100" r="26" role="img" aria-label="Become the Authority icon"/>
          <circle cx="440" cy="100" r="26" role="img" aria-label="Unlock Your Growth icon"/>
          <circle cx="170" cy="195" r="26" role="img" aria-label="Formulate the Follow-Up icon"/>
          <circle cx="305" cy="195" r="26" role="img" aria-label="Construct Your Funnel icon"/>
          <circle cx="440" cy="195" r="26" role="img" aria-label="Develop Lead Generator icon"/>
          <circle cx="170" cy="300" r="26" role="img" aria-label="Clarify the Chaos icon"/>
          <circle cx="305" cy="300" r="26" role="img" aria-label="Define Your Customer icon"/>
          <circle cx="440" cy="300" r="26" role="img" aria-label="Master Your Message icon"/>
        </g>

        <!-- step names -->
        <g fill="#f2d582" font-size="8" font-weight="700" text-anchor="middle">
          <text x="170" y="62">Turn-On the Traffic</text>
          <text x="305" y="62">Become the Authority</text>
          <text x="440" y="62">Unlock Your Growth</text>
          <text x="170" y="157">Formulate the Follow-Up</text>
          <text x="305" y="157">Construct Your Funnel</text>
          <text x="440" y="157">Develop Lead Generator</text>
          <text x="170" y="262">Clarify the Chaos</text>
          <text x="305" y="262">Define Your Customer</text>
          <text x="440" y="262">Master Your Message</text>
        </g>

        <text x="500" y="400" fill="#ffffff" font-size="9" text-anchor="end">Ironvale Keystone Method ©</text>
      </svg>
    </div>
  </div>
</body>
</html>
```